sydney wedding photography business needs a business card design

we need a business card design for a sydney based wedding photography and videography business. our business name is :golden hour photography and video. our target clients are 24-35 yrs female. our style is candid, organic, natural, dynamic. we are a team of young photographers and videographers, and help brides to create memories that they will cherish for the rest of their lives. the logo will be provided. we want an elegant design that reflects our style, and also want to give a great impression to our clients that we are one of the best studios in sydney and our brand means quality and premium service.

Target Market(s)

bride to be, 24-35 years old, living in sydney and surrunding areas

Industry/Entity Type

Wedding Photography

Contact Information for Business Card

address: 57 marrow lane, bexton nsw 2041
mobile: 0431872056
phone: (02) 9361 2748
info@goldenhourstudio.net.au
www.goldenhourstudio.net.au
facebook:goldenhourbridals
instagram:goldenhourbridals

Font styles to use
Serif
Sans Serif

Requirements
Nice to have
• maybe add my slogan"memories beyond eternity" if the layout looks good
Should not have
• no black color, not good idea for wedding biz card

```html
<!DOCTYPE html>
<html lang="en">
<head>
<meta charset="utf-8">
<title>Golden Hour Photography – Business Card</title>
<link rel="stylesheet" href="https://fonts.googleapis.com/css2?family=Montserrat:wght@300;400;500&display=swap">
<style>
  :root {
    --canvas: #ececec;
    --taupe: #6e6266;
    --taupe-back: #756a6d;
    --paper: #ffffff;
    --gold: #d9a01c;
    --blush: #f2a3b3;
    --blush-light: #f7c2cc;
    --blush-deep: #ee98aa;
    --ink-light: #faf5f3;
  }
  * { box-sizing: border-box; margin: 0; padding: 0; }
  html, body {
    width: 1200px; height: 800px; overflow: hidden;
    background: var(--canvas);
    font-family: "Montserrat", sans-serif;
  }
  .sheet {
    position: relative; width: 1200px; height: 800px;
    display: flex; align-items: center; justify-content: center; gap: 40px;
  }
  .card {
    position: relative; width: 540px; height: 330px; overflow: hidden;
    box-shadow: 0 6px 18px rgba(0,0,0,0.15);
  }

  /* Front */
  .card--front { background: var(--blush); }
  .floral-photo {
    position: absolute; inset: 0;
    background: linear-gradient(135deg, var(--blush-light), var(--blush) 55%, var(--blush-deep));
  }
  .brand-box {
    position: absolute; left: 255px; top: 28px; width: 250px; height: 84px;
    background: var(--paper);
    display: flex; align-items: center; justify-content: center; text-align: center;
  }
  .brand-name {
    color: var(--gold); font-weight: 500; text-transform: uppercase;
    letter-spacing: 0.18em; line-height: 1.5;
  }
  .brand-box .brand-name { font-size: 15px; }
  .contact-panel {
    position: absolute; left: 205px; top: 112px; width: 300px; height: 200px;
    background: var(--taupe);
    padding: 16px 18px;
    display: flex; flex-direction: column; justify-content: space-between;
  }
  .contact-row {
    display: flex; align-items: center; gap: 14px;
    color: var(--ink-light); font-weight: 400; font-size: 11.5px; line-height: 1.25;
    white-space: nowrap;
  }
  .contact-icon { width: 16px; height: 16px; flex: none; }
  .contact-icon svg { width: 16px; height: 16px; display: block; }

  /* Back */
  .card--back { background: var(--taupe-back); }
  .back-brand-box {
    position: absolute; left: 100px; top: 80px; width: 340px; height: 120px;
    background: var(--paper);
    display: flex; align-items: center; justify-content: center; text-align: center;
  }
  .back-brand-box .brand-name { font-size: 20px; }
</style>
</head>
<body>
<main class="sheet">

  <section class="card card--front">
    <div class="floral-photo" role="img" aria-label="White roses and green leaves on a soft pink background"></div>

    <div class="brand-box">
      <p class="brand-name">Golden Hour<br>Photography</p>
    </div>

    <div class="contact-panel">
      <div class="contact-row">
        <span class="contact-icon"><svg viewBox="0 0 16 16" fill="none" stroke="#faf5f3" stroke-width="1.4"><path d="M4 2l2 3-1.5 1.5a8 8 0 0 0 5 5L11 10l3 2-1 2.5C7 14 2 9 1.5 3z" stroke-linejoin="round"/></svg></span>
        <span>mobile: 0431872056<br>phone: (02) 9361 2748</span>
      </div>
      <div class="contact-row">
        <span class="contact-icon"><svg viewBox="0 0 16 16" fill="none" stroke="#faf5f3" stroke-width="1.2"><circle cx="8" cy="8" r="6.5"/><ellipse cx="8" cy="8" rx="3" ry="6.5"/><path d="M1.5 8h13M2.5 5h11M2.5 11h11"/></svg></span>
        <span>www.goldenhourstudio.net.au</span>
      </div>
      <div class="contact-row">
        <span class="contact-icon"><svg viewBox="0 0 16 16"><rect x="1" y="3.5" width="14" height="9" fill="#faf5f3"/><path d="M1 3.5l7 5 7-5" fill="none" stroke="#6e6266" stroke-width="1.2"/></svg></span>
        <span>info@goldenhourstudio.net.au</span>
      </div>
      <div class="contact-row">
        <span class="contact-icon"><svg viewBox="0 0 16 16"><path d="M8 15s5-5.5 5-9A5 5 0 0 0 3 6c0 3.5 5 9 5 9z" fill="#faf5f3"/><circle cx="8" cy="6" r="1.8" fill="#6e6266"/></svg></span>
        <span>57 marrow lane, bexton nsw 2041</span>
      </div>
      <div class="contact-row">
        <span class="contact-icon"><svg viewBox="0 0 16 16"><circle cx="8" cy="8" r="7" fill="#faf5f3"/></svg></span>
        <span>/goldenhourbridals</span>
      </div>
      <div class="contact-row">
        <span class="contact-icon"><svg viewBox="0 0 16 16"><circle cx="8" cy="8" r="7" fill="#faf5f3"/></svg></span>
        <span>/goldenhourbridals</span>
      </div>
    </div>
  </section>

  <section class="card card--back">
    <div class="back-brand-box">
      <p class="brand-name">Golden Hour<br>Photography</p>
    </div>
  </section>

</main>
</body>
</html>
```